Need A Homepage Redesign For Ecommerce Store

Just looking for a great quality designer to redesign my homepage. We will take current structure and redesign to make it cleaner and more user friendly.

Our website is here - www.brivonelfilters.com

Please see the attached for the layout structure that we would like. Please be creative as well.

As you can see the current design does not look clean and is not user friendly.

See attached and thank you and good luck!

P.S. Whoever wins I will give them the next work for product pages and other landing pages.

Target Market(s)

Middle to upper class health minded people, ages 30 and up

Industry/Entity Type

Health And Wellness

Number of Pages Required

1 page

Font styles to use
Sans Serif

Colors
0255a3
0792cd
00a990

Requirements
Must have
• Clean design. Professional design. Use current logo and tagline (unless you think you can do better).
Nice to have
• I would like to see some creativity as well.
Should not have
• Please dont use the same structure as I have. Want this to be a total redesign.

```html
<!DOCTYPE html>
<html lang="en">
<head>
<meta charset="utf-8">
<title>Brivonel Water Ionizers – Help Deciding</title>
<link rel="stylesheet" href="https://fonts.googleapis.com/css2?family=Open+Sans:wght@400;600;700;800&display=swap">
<style>
  :root {
    --brand-blue: #0792cd;
    --heading-blue: #1689cc;
    --card-tint: #3aa8d8;
    --card-tint-deep: #2f9dcf;
    --white: #ffffff;
    --button-bg: #f1f3f5;
    --photo-sky-top: #3f6f9e;
    --photo-sky-mid: #8fb4d2;
    --photo-water: #4f7fa8;
  }
  * { margin: 0; padding: 0; box-sizing: border-box; }
  html, body {
    width: 1125px; height: 1200px; overflow: hidden;
    background: var(--white);
    font-family: "Open Sans", Arial, sans-serif;
  }
  .page { position: relative; width: 1125px; height: 1200px; }

  .section-title {
    position: absolute; left: 0; width: 1125px;
    text-align: center; color: var(--heading-blue);
    font-weight: 800; font-size: 25px; line-height: 30px;
    letter-spacing: 0.3px; text-transform: uppercase;
  }
  .section-title.help { top: 48px; }
  .section-title.confidence { top: 572px; }

  .card {
    position: absolute; top: 157px; width: 402px; height: 348px;
    background: linear-gradient(160deg, var(--card-tint) 0%, var(--card-tint-deep) 100%);
    color: var(--white); text-align: center; overflow: hidden;
  }
  .card.reviews { left: 145px; }
  .card.compare { left: 575px; }
  .card-photo { position: absolute; inset: 0; }
  .card-frame {
    position: absolute; inset: 10px;
    border: 2px solid rgba(255,255,255,0.7);
  }
  .card-body { position: absolute; left: 0; right: 0; }
  .card.reviews .card-body { top: 110px; }
  .card.compare .card-body { top: 130px; }
  .card-title {
    font-weight: 800; font-size: 17.5px; line-height: 21.5px;
  }
  .card-quote {
    margin: 16px auto 0; width: 300px;
    font-size: 11.2px; line-height: 14px; font-weight: 400;
  }
  .card-button {
    display: inline-block; margin-top: 17px;
    background: var(--button-bg); color: var(--brand-blue);
    font-weight: 700; font-size: 11.5px; line-height: 31px;
    height: 31px; border-radius: 5px; text-decoration: none;
  }
  .card.reviews .card-button { width: 104px; }
  .card.compare .card-button { width: 161px; margin-top: 44px; }

  .warranty-band {
    position: absolute; left: 0; top: 683px; width: 1125px; height: 467px;
    background: var(--brand-blue);
  }
  .warranty-photo {
    position: absolute; left: 0; top: 0; width: 540px; height: 467px;
    background: linear-gradient(180deg, var(--photo-sky-top) 0%, var(--photo-sky-mid) 55%, var(--photo-water) 75%, #8fb3d0 100%);
  }
  .warranty-text {
    position: absolute; left: 655px; top: 168px;
    color: var(--white); font-weight: 600; font-size: 18.5px; line-height: 24px;
    letter-spacing: 0.5px;
  }
  .warranty-text p + p { margin-top: 24px; }
</style>
</head>
<body>
<main class="page">
  <h2 class="section-title help">Still need help deciding right<br>alkaline water machine?</h2>

  <article class="card reviews">
    <div class="card-photo" role="img" aria-label="Smiling woman holding a glass of water, tinted blue"
         style="background: radial-gradient(ellipse 90px 150px at 68% 40%, rgba(255,255,255,0.10), transparent 70%);"></div>
    <div class="card-frame"></div>
    <div class="card-body">
      <h3 class="card-title">What Are People Saying About<br>Brivonel Water Ionizers?</h3>
      <p class="card-quote">“For The Quality Of This Ionizer, I would Have Expected To Pay Double What I Ended Up Paying For.Customer Service Was Amazing.<br>Highly Recommended!”</p>
      <a class="card-button" href="#">See More</a>
    </div>
  </article>

  <article class="card compare">
    <div class="card-photo" role="img" aria-label="Countertop water ionizer machine, tinted blue"
         style="background: linear-gradient(90deg, transparent 15%, rgba(10,50,90,0.18) 25%, rgba(10,50,90,0.22) 82%, transparent 88%);"></div>
    <div class="card-frame"></div>
    <div class="card-body">
      <h3 class="card-title">Find The<br>Right Water<br>Ionizer For You</h3>
      <a class="card-button" href="#">Compare Water Ionizer</a>
    </div>
  </article>

  <h2 class="section-title confidence">Shop with confidence-our water<br>ionizers are simply the best!</h2>

  <section class="warranty-band">
    <div class="warranty-photo" role="img" aria-label="Water pouring into a glass against a blue sky and lake"></div>
    <div class="warranty-text">
      <p>Quality-Our Brivonel Water Ionizers<br>Are Backed By Our Lifetime Warranty.</p>
      <p>We Will Ensure Your Water Ionizer<br>Works For Life, Guaranteed!</p>
    </div>
  </section>
</main>
</body>
</html>
```